A Dedicated Thank You to my Dad

Proposed Dimensions: Approx. 20" x 30"

For Father's Day, I wrote a dedication to my Dad that encapsulates my gratitude for everything he does, and everything he is. His birthday is on August 3, but it is more important for me to transform this dedication into a meaningful and memorable gift than to meet any deadline. I would love an image that captures the relationship between a father and his son, accompanied by my words of thanks in some sort of font that is appropriate for the message (calligprahy? not sure about that).

I had actually posted the Thank You on Pixelmarrow as a public post, so anyone with an account can read it: https://www.pixelmarrow.example/photo.php?fbid=40872219360548813&set=a.318760942157.6650129.3908471&type=1&theater

Only the words starting with "Thank you ..." should be on the poster.

Target Market(s)

This is a personal gift for my Dad. He doesn't have the best of eyesight, so having the words in a really small font would not be particularly helpful. :-)

Requirements
Must have
• * Personable
* Warm
* Inviting
* Memorable
* Understated more favored over Loud
Should not have
• * An entire palette of colors
* Wacky colors or fonts

```html
<!DOCTYPE html>
<html lang="en">
<head>
<meta charset="utf-8">
<title>Happy Father's Day – The Best Dad</title>
<link rel="stylesheet" href="https://fonts.googleapis.com/css2?family=Great+Vibes&family=Pinyon+Script&family=Cinzel:wght@700&display=swap">
<style>
  :root {
    --page: #ffffff;
    --sky-top: #4a1a3a;
    --sky-mid: #b8421e;
    --sky-glow: #e8892a;
    --horizon: #ffd27a;
    --sand: #d9822e;
    --sand-deep: #7a3512;
    --edge: #3a0f12;
    --frame-line: #ffb07a;
    --ribbon: #a8231f;
    --ribbon-ink: #fbe9dc;
    --title-top: #ff8a3c;
    --title-bottom: #fff0a8;
    --body-ink: #fff6ea;
    --date-ink: #ffd21c;
    --signoff: #e0a05a;
    --ring-magenta: #d4207a;
    --ring-pink: #f06aa8;
    --ring-green: #8ccf3a;
    --ring-orange: #f59a2a;
    --photo-fill-a: #b9a48e;
    --photo-fill-b: #6e5a4c;
  }
  * { margin: 0; padding: 0; box-sizing: border-box; }
  html, body { width: 828px; height: 1200px; overflow: hidden; background: var(--page); }
  .canvas { position: relative; width: 828px; height: 1200px; background: var(--page); }
  .poster {
    position: absolute; left: 42px; top: 40px; width: 746px; height: 1120px; overflow: hidden;
  }
  .sunset-scene {
    position: absolute; inset: 0;
    background:
      radial-gradient(ellipse 240px 70px at 62% 56%, var(--horizon) 0%, rgba(255,210,122,0) 100%),
      radial-gradient(ellipse 140px 260px at 55% 72%, rgba(40,15,10,0.35) 0%, rgba(40,15,10,0) 100%),
      linear-gradient(180deg, var(--sky-top) 0%, var(--sky-mid) 22%, var(--sky-glow) 42%, var(--horizon) 55%, var(--sand) 64%, var(--sand-deep) 86%, var(--edge) 100%);
  }
  .frame {
    position: absolute; left: 26px; top: 22px; width: 694px; height: 1072px;
    border: 2px solid var(--frame-line); border-radius: 26px; opacity: 0.85;
  }
  .ribbon { position: absolute; left: 319px; top: 0; width: 107px; height: 106px; }
  .ribbon-label {
    position: absolute; left: 0; top: 14px; width: 107px; text-align: center;
    font-family: "Cinzel", serif; font-size: 28px; color: var(--ribbon-ink);
  }
  .ribbon-label svg { vertical-align: -3px; margin-left: 4px; }
  .title {
    position: absolute; left: 0; width: 746px; text-align: center;
    font-family: "Great Vibes", cursive; line-height: 1;
    background: linear-gradient(180deg, var(--title-top), var(--title-bottom));
    -webkit-background-clip: text; background-clip: text; color: transparent;
  }
  .title-happy { top: 150px; font-size: 140px; margin-left: -20px; }
  .title-fathers { top: 268px; font-size: 150px; margin-left: -10px; }
  .title-day { top: 386px; font-size: 140px; margin-left: 10px; }
  .portrait { position: absolute; width: 210px; height: 210px; }
  .portrait-son { left: 75px; top: 539px; }
  .portrait-parents { left: 177px; top: 671px; }
  .body-copy {
    position: absolute; left: 0; top: 910px; width: 746px; text-align: center;
    font-family: "Pinyon Script", cursive; font-size: 19px; line-height: 22px; color: var(--body-ink);
  }
  .body-copy .date { color: var(--date-ink); }
  .signoff {
    position: absolute; left: 0; top: 1026px; width: 746px; display: flex; justify-content: center; align-items: center; gap: 18px;
    font-family: "Cinzel", serif; font-size: 18px; letter-spacing: 4px; color: var(--signoff);
  }
  .signoff-rule { width: 60px; height: 1px; background: var(--signoff); }
</style>
</head>
<body>
<main class="canvas">
  <section class="poster">
    <div class="sunset-scene" role="img" aria-label="Beach at sunset with a father and small son walking hand in hand along the shore"></div>
    <div class="frame"></div>

    <div class="ribbon">
      <svg width="107" height="106" viewBox="0 0 107 106">
        <path d="M0 0H107V106L98 98L89 106L80 98L71 106L62 98L53 106L44 98L35 106L26 98L17 106L8 98L0 106Z" fill="var(--ribbon)"/>
        <line x1="16" y1="86" x2="91" y2="86" stroke="var(--ribbon-ink)" stroke-width="1" stroke-dasharray="3 3" opacity="0.7"/>
      </svg>
      <div class="ribbon-label">I<svg width="26" height="24" viewBox="0 0 26 24"><path d="M13 23C5 16 0 11 0 6.5 0 3 3 0 6.5 0 9.5 0 12 2 13 4 14 2 16.5 0 19.5 0 23 0 26 3 26 6.5 26 11 21 16 13 23Z" fill="var(--ribbon-ink)"/></svg></div>
    </div>

    <div class="title title-happy">Happy</div>
    <div class="title title-fathers">Father's</div>
    <div class="title title-day">Day</div>

    <svg class="portrait portrait-son" viewBox="0 0 210 210">
      <circle cx="105" cy="105" r="103" fill="none" stroke="var(--ring-pink)" stroke-width="2"/>
      <circle cx="105" cy="105" r="98" fill="none" stroke="var(--ring-magenta)" stroke-width="5"/>
      <circle cx="105" cy="105" r="91" fill="none" stroke="var(--ring-orange)" stroke-width="3"/>
      <circle cx="105" cy="105" r="86" fill="none" stroke="var(--ring-green)" stroke-width="5"/>
      <circle cx="105" cy="105" r="82" fill="var(--photo-fill-a)" role="img" aria-label="Photo of the son and his father together"/>
    </svg>
    <svg class="portrait portrait-parents" viewBox="0 0 210 210">
      <circle cx="105" cy="105" r="103" fill="none" stroke="var(--ring-pink)" stroke-width="2"/>
      <circle cx="105" cy="105" r="98" fill="none" stroke="var(--ring-magenta)" stroke-width="5"/>
      <circle cx="105" cy="105" r="91" fill="none" stroke="var(--ring-orange)" stroke-width="3"/>
      <circle cx="105" cy="105" r="86" fill="none" stroke="var(--ring-green)" stroke-width="5"/>
      <circle cx="105" cy="105" r="82" fill="var(--photo-fill-b)" role="img" aria-label="Photo of the father with his wife"/>
    </svg>

    <p class="body-copy">
      I wrote a dedication to my Dad that encapsulates my gratitude<br>
      foreverything he does, and everything he is.<br>
      His birthday is on <span class="date">August 3</span>, but it is more important for me to transform<br>
      this dedication into a meaningful and memorable gift
    </p>

    <div class="signoff"><span class="signoff-rule"></span>THE BEST DAD<span class="signoff-rule"></span></div>
  </section>
</main>
</body>
</html>
```